SaaS startup seeking website design and build on Vornix.io

Need a website designed and built on Vornix.io for a new SaaS startup called PeakMoor (logo provided).

***The winning designer will be provided with a login to our Vornix.io subscription to deploy the design - please only submit a design if you are familiar with the Vornix platform. ***

The business will be selling a cloud-based system for customer success management; a tool to ensure SaaS businesses successfully onboard, retain for renewals, upsell and cross-sell to existing customers. Logo and colour guide provided, pages required in the design:
Home,
Tour,
Pricing,
Blog,
Contact

Require buttons/ forms for
Login,
Sign-up for Trial,
Sign-up for Newsletter,
Request Demo,
Contact Us.

The winning designer will be provided with a login to our Vornix.io subscription to deploy the design - please only submit a design if you are familiar with the Vornix platform. Draft designs submitted on trial vornix accounts will also be considered.

Seek inspiration and placeholder content from https://tallowbrim.net/
https://www.quimerra.com/
https://fernwhistle.com/

Target Market(s)

SaaS companies

Coding

Coded - Design and coding required

Number of Pages Required

1 page

```html
<!DOCTYPE html>
<html lang="en">
<head>
<meta charset="utf-8">
<title>PeakMoor – Customer Success Platform</title>
<link href="https://fonts.googleapis.com/css2?family=Open+Sans:wght@400;600;700&family=Playfair+Display:wght@700&display=swap" rel="stylesheet">
<style>
:root{
  --navy:#233b63;
  --navy-deep:#1a2d4d;
  --ink:#1f3354;
  --blue:#2f8fd6;
  --blue-dark:#1e6fb0;
  --sky:#dbeaf6;
  --sky-soft:#eaf3fa;
  --text:#5d6878;
  --muted:#9aa5b3;
  --line:#e2e7ee;
  --white:#ffffff;
}
*{box-sizing:border-box;margin:0;padding:0}
html,body{width:1200px;height:4620px;overflow:hidden}
body{font-family:"Open Sans",Arial,sans-serif;color:var(--text);background:var(--white);position:relative}
.abs{position:absolute}
.btn{display:inline-block;border-radius:20px;font-weight:600;color:var(--white);text-align:center;font-size:13px}

/* nav */
.nav{top:0;left:0;width:1200px;height:60px;background:var(--white)}
.brand{left:28px;top:12px;display:flex;align-items:center;gap:10px;font-size:28px;font-weight:700;color:var(--navy)}
.brand-dot{width:22px;height:22px;background:var(--blue);border-radius:50%}
.nav-links{left:624px;top:20px;display:flex;gap:36px;font-size:14px;color:var(--ink)}
.nav-login{left:880px;top:14px;width:72px;height:32px;line-height:32px;background:var(--navy)}
.nav-signup{left:966px;top:14px;width:80px;height:32px;line-height:32px;background:var(--blue)}

/* hero */
.hero{top:60px;left:0;width:1200px;height:540px}
.hero-title{left:140px;top:150px;width:380px;font-size:31px;font-weight:700;color:var(--white);line-height:1.25}
.hero-sub{left:140px;top:285px;width:360px;font-size:13px;color:#c9d6e8;line-height:1.6}
.hero-form{left:140px;top:395px;width:400px;height:46px;border:2px solid #3f9ae0;border-radius:24px;background:var(--white)}
.hero-placeholder{position:absolute;left:22px;top:13px;font-size:13px;color:var(--muted)}
.hero-cta{position:absolute;right:2px;top:2px;width:140px;height:38px;line-height:38px;background:var(--blue)}
.hero-shot{left:620px;top:180px;width:390px;height:250px;border-radius:8px;background:linear-gradient(180deg,#f4f7fb,#dfe7f1);box-shadow:0 10px 30px rgba(0,0,0,.3)}

/* press */
.press{top:730px;left:140px;width:920px;display:flex;justify-content:space-between;align-items:center;color:#3a3a3a;font-family:"Playfair Display",Georgia,serif;font-weight:700;font-size:24px}
.divider{top:875px;left:0;width:1200px;height:1px;background:var(--line)}

/* features */
.feat-title{font-size:30px;font-weight:700;color:var(--navy)}
.feat-lead{font-size:14px;line-height:1.6;width:370px}
.item{display:flex;gap:18px;width:380px}
.icon{width:46px;height:46px;flex:none;background:var(--sky);border-radius:4px;display:flex;align-items:center;justify-content:center}
.item h4{font-size:15px;color:var(--ink);margin-bottom:4px}
.item p{font-size:11px;line-height:1.5}
.shot{border-radius:4px;background:linear-gradient(180deg,#f7f9fc,#e4ebf3);box-shadow:0 6px 24px rgba(30,50,80,.18)}

/* pricing */
.pricing-title{top:2625px;left:0;width:1200px;text-align:center;font-size:32px;font-weight:700;color:var(--navy)}
.pricing-sub{top:2680px;left:0;width:1200px;text-align:center;font-size:20px;color:var(--ink)}
.card{top:2735px;width:300px;height:380px;background:var(--white);box-shadow:0 6px 20px rgba(30,50,80,.12);text-align:center;padding:20px 22px}
.card h3{font-size:28px;font-weight:600;color:var(--navy)}
.card .blurb{font-size:11px;line-height:1.5;margin:8px 0 14px}
.price{font-size:64px;font-weight:600;color:var(--blue);line-height:1}
.price small{font-size:22px;color:var(--muted);font-weight:400}
.perks{list-style:none;text-align:left;margin:26px 0 0;font-size:11px}
.perks li{padding:9px 0;border-top:1px solid var(--line);display:flex;gap:8px;align-items:center}
.perks li:before{content:"";width:8px;height:8px;border-radius:50%;background:var(--blue)}
.card .btn{width:256px;height:34px;line-height:34px;background:var(--blue);margin-top:18px}

/* contact */
.contact-title{top:3325px;left:0;width:1200px;text-align:center;font-size:34px;font-weight:700;color:var(--blue)}
.contact-sub{top:3385px;left:0;width:1200px;text-align:center;font-size:20px;color:#d6e0ee}
.label{font-size:13px;color:var(--white)}
.field{height:50px;border:1px solid #5d7bb0;background:rgba(255,255,255,.04);font-size:12px;color:#7189b3;padding:16px 12px}
.send{top:3846px;left:526px;width:150px;height:38px;line-height:38px;background:var(--blue)}

/* cta */
.cta-title{top:4110px;left:0;width:1200px;text-align:center;font-size:32px;font-weight:700;color:var(--navy)}
.cta-sub{top:4165px;left:0;width:1200px;text-align:center;font-size:20px;color:var(--ink)}
.cta-a{top:4215px;left:428px;width:164px;height:52px;line-height:52px;border-radius:26px;background:var(--navy);font-size:14px}
.cta-b{top:4215px;left:608px;width:164px;height:52px;line-height:52px;border-radius:26px;background:var(--blue);font-size:14px}

/* footer */
.foot-copy{top:4460px;left:140px;font-size:12px;color:#b7c3d4;line-height:1.6}
.social{top:4530px;left:140px;display:flex;gap:14px}
.social span{width:18px;height:18px;border-radius:50%;background:#c5d1e2}
.foot-col{top:4455px;font-size:12px;color:#c5d1e2;line-height:2.1}
</style>
</head>
<body>

<!-- navigation -->
<header class="abs nav">
  <div class="abs brand"><span class="brand-dot"></span>PeakMoor</div>
  <nav class="abs nav-links"><span>Features</span><span>Pricing</span><span>FAQ</span></nav>
  <span class="abs btn nav-login">Login</span>
  <span class="abs btn nav-signup">Sign Up</span>
</header>

<!-- hero background -->
<svg class="abs hero" viewBox="0 0 1200 540" width="1200" height="540">
  <defs>
    <linearGradient id="heroGrad" x1="0" y1="0" x2="1" y2="1">
      <stop offset="0" stop-color="#2a4575"/>
      <stop offset="1" stop-color="#1f3761"/>
    </linearGradient>
  </defs>
  <path d="M0 0H1200V420L0 540Z" fill="url(#heroGrad)"/>
</svg>
<h1 class="abs hero-title">Spark Interest: What makes your product desirable?</h1>
<p class="abs hero-sub">Use this space to tell the customer how your product works and why it is different.</p>
<div class="abs hero-form"><span class="hero-placeholder">email@example.com</span><span class="btn hero-cta">GET STARTED</span></div>
<div class="abs hero-shot" role="img" aria-label="Laptop showing the PeakMoor customer success dashboard"></div>

<!-- press -->
<div class="abs press">
  <span>Venturist</span><span>Harlow</span><span>Brightmark</span><span>Ledger 500</span><span>The Morning Dispatch</span>
</div>
<div class="abs divider"></div>

<!-- feature 1 -->
<h2 class="abs feat-title" style="top:925px;left:140px">Aliquam erat volutpat</h2>
<p class="abs feat-lead" style="top:975px;left:140px">Nullam lorem urna, tempus eget mollis et, dapibus ac sem. Suspendisse gravida ornare pulvinar. Vestibulum luctus ex in egestas fringilla.</p>
<div class="abs item" style="top:1085px;left:140px"><span class="icon"><svg width="22" height="22" viewBox="0 0 22 22"><path d="M3 18L9 11l4 4 6-8" stroke="#1f3354" stroke-width="2" fill="none"/></svg></span><div><h4>Mauris bibendum</h4><p>Nulla in lorem sit purus pellentesque posuere. Nulla tristique purus nisi molestie, aliquam erat volutpat.</p></div></div>
<div class="abs item" style="top:1170px;left:140px"><span class="icon"><svg width="22" height="22" viewBox="0 0 22 22"><rect x="3" y="4" width="16" height="14" stroke="#1f3354" stroke-width="2" fill="none"/></svg></span><div><h4>Duis ornare erat</h4><p>Nulla in lorem sit purus pellentesque posuere. Nulla tristique purus nisi molestie, aliquam erat volutpat.</p></div></div>
<div class="abs item" style="top:1255px;left:140px"><span class="icon"><svg width="22" height="22" viewBox="0 0 22 22"><circle cx="11" cy="8" r="4" fill="#1f3354"/><path d="M3 20a8 7 0 0 1 16 0Z" fill="#1f3354"/></svg></span><div><h4>Nam tempus</h4><p>Nulla in lorem sit purus pellentesque posuere. Nulla tristique purus nisi molestie, aliquam erat volutpat.</p></div></div>
<div class="abs shot" style="top:1015px;left:705px;width:360px;height:270px" role="img" aria-label="Screenshot of the account health chart view"></div>

<!-- feature 2 -->
<div class="abs shot" style="top:1550px;left:140px;width:360px;height:215px" role="img" aria-label="Screenshot of the customer timeline view"></div>
<h2 class="abs feat-title" style="top:1455px;left:650px">Pellentesque blandit</h2>
<p class="abs feat-lead" style="top:1505px;left:650px">Nullam lorem urna, tempus eget mollis et, dapibus ac sem. Suspendisse gravida ornare pulvinar. Vestibulum luctus ex in egestas fringilla.</p>
<div class="abs item" style="top:1615px;left:650px"><span class="icon"><svg width="22" height="22" viewBox="0 0 22 22"><path d="M2 8h10v8H2zM12 11h5l3 3v2h-8z" fill="#1f3354"/></svg></span><div><h4>Cras eget leo</h4><p>Nulla in lorem sit purus pellentesque posuere. Nulla tristique purus nisi molestie, aliquam erat volutpat.</p></div></div>
<div class="abs item" style="top:1700px;left:650px"><span class="icon"><svg width="22" height="22" viewBox="0 0 22 22"><rect x="6" y="2" width="10" height="18" rx="2" stroke="#1f3354" stroke-width="2" fill="none"/></svg></span><div><h4>Praesent iaculis</h4><p>Nulla in lorem sit purus pellentesque posuere. Nulla tristique purus nisi molestie, aliquam erat volutpat.</p></div></div>
<div class="abs item" style="top:1785px;left:650px"><span class="icon"><svg width="22" height="22" viewBox="0 0 22 22"><circle cx="11" cy="11" r="8" fill="#1f3354"/><path d="M11 11V3A8 8 0 0 1 19 11Z" fill="#9cc7ea"/></svg></span><div><h4>Maecenas consequat</h4><p>Nulla in lorem sit purus pellentesque posuere. Nulla tristique purus nisi molestie, aliquam erat volutpat.</p></div></div>

<!-- feature 3 -->
<h2 class="abs feat-title" style="top:1955px;left:140px">Phasellus consequat</h2>
<p class="abs feat-lead" style="top:2005px;left:140px">Nullam lorem urna, tempus eget mollis et, dapibus ac sem. Suspendisse gravida ornare pulvinar. Vestibulum luctus ex in egestas fringilla.</p>
<div class="abs item" style="top:2120px;left:140px"><span class="icon"><svg width="22" height="22" viewBox="0 0 22 22"><path d="M3 18L9 11l4 4 6-8" stroke="#1f3354" stroke-width="2" fill="none"/></svg></span><div><h4>Sed augue orci</h4><p>Nulla in lorem sit purus pellentesque posuere. Nulla tristique purus nisi molestie, aliquam erat volutpat.</p></div></div>
<div class="abs item" style="top:2205px;left:140px"><span class="icon"><svg width="22" height="22" viewBox="0 0 22 22"><rect x="3" y="4" width="16" height="14" fill="#1f3354"/></svg></span><div><h4>Aliquam consectetur</h4><p>Nulla in lorem sit purus pellentesque posuere. Nulla tristique purus nisi molestie, aliquam erat volutpat.</p></div></div>
<div class="abs item" style="top:2290px;left:140px"><span class="icon"><svg width="22" height="22" viewBox="0 0 22 22"><circle cx="11" cy="11" r="8" fill="#1f3354"/></svg></span><div><h4>Proin eget congue</h4><p>Nulla in lorem sit purus pellentesque posuere. Nulla tristique purus nisi molestie, aliquam erat volutpat.</p></div></div>
<div class="abs shot" style="top:2065px;left:705px;width:360px;height:260px" role="img" aria-label="Screenshot of the renewals pipeline view"></div>

<!-- pricing background -->
<svg class="abs" style="top:2450px;left:0" width="1200" height="720" viewBox="0 0 1200 720">
  <path d="M0 110L1200 0V720H0Z" fill="#dcebf7"/>
</svg>
<h2 class="abs pricing-title">Simple, transparent pricing.</h2>
<p class="abs pricing-sub">Always know what you'll Pay</p>
<div class="abs card" style="left:140px"><h3>Vestibulum</h3><p class="blurb">Pellentesque a imperdiet dolor, ut cursus nisi. Lorem sollicitudin tortor at felis ultrices.</p><div class="price">$49<small> / mo</small></div><ul class="perks"><li>Proin placerat dapibus</li><li>Maecenas vel tortor accumsan</li><li>Aenean facilisis tincidunt</li></ul><span class="btn">Sign Up</span></div>
<div class="abs card" style="left:450px"><h3>Praesent</h3><p class="blurb">Pellentesque a imperdiet dolor, ut cursus nisi. Lorem sollicitudin tortor at felis ultrices.</p><div class="price">$99<small> / mo</small></div><ul class="perks"><li>Proin placerat dapibus</li><li>Maecenas vel tortor accumsan</li><li>Aenean facilisis tincidunt</li></ul><span class="btn">Sign Up</span></div>
<div class="abs card" style="left:760px"><h3>Fusce vitae</h3><p class="blurb">Pellentesque a imperdiet dolor, ut cursus nisi. Lorem sollicitudin tortor at felis ultrices.</p><div class="price">$199<small> / mo</small></div><ul class="perks"><li>Proin placerat dapibus</li><li>Maecenas vel tortor accumsan</li><li>Aenean facilisis tincidunt</li></ul><span class="btn">Sign Up</span></div>

<!-- contact -->
<div class="abs" style="top:3170px;left:0;width:1200px;height:760px;background:var(--navy)"></div>
<h2 class="abs contact-title">Contact us</h2>
<p class="abs contact-sub">Got any questions? Don't hesitate to reach out.</p>
<span class="abs label" style="top:3445px;left:318px">Full Name</span>
<div class="abs field" style="top:3470px;left:318px;width:564px">Jane Doe</div>
<span class="abs label" style="top:3548px;left:318px">Email Address</span>
<div class="abs field" style="top:3573px;left:318px;width:272px">jane.doe@mail.com</div>
<span class="abs label" style="top:3548px;left:610px">Phone (Optional)</span>
<div class="abs field" style="top:3573px;left:610px;width:272px">(123) 456-7890</div>
<span class="abs label" style="top:3652px;left:318px">Your Message</span>
<div class="abs field" style="top:3677px;left:318px;width:564px;height:145px"></div>
<span class="abs btn send">SEND MESSAGE</span>

<!-- cta -->
<svg class="abs" style="top:3930px;left:0" width="1200" height="120" viewBox="0 0 1200 120">
  <path d="M0 0H1200L0 110Z" fill="#233b63"/>
</svg>
<h2 class="abs cta-title">Ready to get started?</h2>
<p class="abs cta-sub">Contact us or sign up now.</p>
<span class="abs btn cta-a">GET STARTED</span>
<span class="abs btn cta-b">CONTACT US</span>

<!-- footer -->
<svg class="abs" style="top:4300px;left:0" width="1200" height="320" viewBox="0 0 1200 320">
  <path d="M0 40L1200 0V320H0Z" fill="#1a2d4d"/>
</svg>
<p class="abs foot-copy">Copyright © 2020 PeakMoor.<br>All rights reserved.</p>
<div class="abs social"><span></span><span></span><span></span></div>
<div class="abs foot-col" style="left:700px">Product<br>Features<br>Pricing<br>Tour</div>
<div class="abs foot-col" style="left:825px">Company<br>About<br>Team<br>Blog</div>
<div class="abs foot-col" style="left:950px">Legal<br>Terms of Service<br>Privacy Policy<br>GDPR Policy</div>

</body>
</html>
```